Simple and clean

We need a business card design for a new company called Dwelling Owl. It is a search engine to find current properties for sale or rent in New Zealand market.
We have already a colour scheme that we would like people to use.
Light brown: #D4CCB0
Light green: #D6E4D4
Green: #669966
Black/White
It is OK to divert from this colour scheme slightly as long as there is a green component to the business card.
Final design should be clean, simple and should communicate the nature of the business.
Target Market(s)
- First home buyers
- Real estate agents
- People seeking rentals
Industry/Entity Type
Business
Requirements
Must have
- Use those or similar colours.
Light brown: #D4CCB0
Light green: #D6E4D4
Green: #669966
Black/White

```html
<!DOCTYPE html>
<html lang="en">
<head>
<meta charset="utf-8">
<title>Dwelling Owl — Business Card</title>
<link href="https://fonts.googleapis.com/css2?family=Arimo:wght@400;700&family=Jost:wght@400;500&display=swap" rel="stylesheet">
<style>
  :root {
    --page-bg: #ececea;
    --card-cream: #fbf8e9;
    --brand-green: #669966;
    --text-green: #5f955f;
    --band-black: #1c1c1a;
    --logo-cream: #f3efdc;
  }
  * { margin: 0; padding: 0; box-sizing: border-box; }
  html, body {
    width: 1200px;
    height: 1200px;
    overflow: hidden;
    background: var(--page-bg);
  }
  .canvas {
    position: relative;
    width: 1200px;
    height: 1200px;
  }
  .business-card {
    position: absolute;
    left: 117px;
    top: 325px;
    width: 966px;
    height: 550px;
    background: var(--card-cream);
    overflow: hidden;
    box-shadow: 0 2px 10px rgba(0, 0, 0, 0.12);
  }
  .card-shapes {
    position: absolute;
    inset: 0;
    width: 966px;
    height: 550px;
  }
  .contact-block {
    position: absolute;
    left: 123px;
    top: 70px;
    color: var(--text-green);
  }
  .contact-name {
    font-family: "Jost", sans-serif;
    font-weight: 500;
    font-size: 46px;
    line-height: 1;
    letter-spacing: 0.5px;
    margin-bottom: 12px;
  }
  .contact-line {
    font-family: "Arimo", sans-serif;
    font-size: 38px;
    line-height: 45px;
  }
  .contact-web {
    font-weight: 700;
  }
  .brand-lockup {
    position: absolute;
    left: 27px;
    top: 422px;
    display: flex;
    align-items: center;
    gap: 14px;
  }
  .brand-dot {
    width: 72px;
    height: 72px;
    border-radius: 50%;
    background: var(--brand-green);
  }
  .brand-name {
    font-family: "Jost", sans-serif;
    font-weight: 400;
    font-size: 56px;
    color: var(--logo-cream);
    line-height: 1;
  }
</style>
</head>
<body>
  <main class="canvas">
    <section class="business-card">
      <svg class="card-shapes" viewBox="0 0 966 550" aria-hidden="true">
        <line class="name-rule" x1="380" y1="106" x2="966" y2="106" stroke="#669966" stroke-width="2"/>
        <polygon class="accent-wedge" points="513,455 966,371 966,503" fill="#669966"/>
        <polygon class="base-band" points="0,371 513,455 966,503 966,550 0,550" fill="#1c1c1a"/>
      </svg>

      <div class="contact-block">
        <p class="contact-name">Mark Ellery</p>
        <p class="contact-line contact-role">Developer</p>
        <p class="contact-line contact-phone">0521847306</p>
        <p class="contact-line contact-email">mark@ellery.net</p>
        <p class="contact-line contact-web">www.dwellingowl.co.nz</p>
      </div>

      <div class="brand-lockup">
        <span class="brand-dot"></span>
        <span class="brand-name">Dwelling Owl</span>
      </div>
    </section>
  </main>
</body>
</html>
```